Brochure flyer for handout and web distribution - 11 X 17 folded four pages 8.5 X 11

We need a brochure for trade shows. Title page is "When Speed To Market Counts - We Deliver"- company logos on bottom of the page.

We build cannabis grow facilities and can build 3-6 months faster than conventional building methods. We want to use green as a focus color. We have an image cannabis interactive that we want to have in the center fold. It comes from this webpage which has the building descriptions - https://www.tallowfen.com/cannabis-buildings

Also attached is an ad from Hempvora we did for a previous show that shows how I would like logos on the back cover - without the background image and without the text - replace text on back page with file attached with key advantages that we would like on the back page as well.

There are also some images from our partner MeltaBrook that we would love to show on the inside cover as well - so one page is Brevik interactive and buildings and the other inside page features MeltaBrook.

For content on Melta-Brook - When choosing between modular construction and traditionally constructed rooms, consider that all modular construction is objectively faster and more affordable. On average you can cut construction time by half when using a modular room and building design compared to conventionally construction. All components used to construct modular rooms and buildings have already been designed and fabricated at our plant, causing:
• Less disruption to your daily business operations
• Less construction waste and debris
Logos are attached for the back page - these can also be used on the front page. Website is www.rivenstalkworks.com (visit us). Contact us at info@rivenstalkworks.com

All images can be provided EPS - final design will need to be 300DPI minimum

Target Market(s)

Lead investors in Cannabis

Industry/Entity Type

Cannabis Industry

Font styles to use
Serif

Colors
0094D4
00A9DD
6FCCEA
C7EBF8
E9F6FB
00AB8E
00BBA5
67D7C9
C6EFE9
E9F9F6

Requirements
Must have
• Logos, website, 4 pages
Should not have
• Cannabis images

```html
<!DOCTYPE html>
<html lang="en">
<head>
<meta charset="utf-8">
<title>Norvane Enterprises – Trade Show Brochure</title>
<link rel="stylesheet" href="https://fonts.googleapis.com/css2?family=Montserrat:wght@300;400;500;600;700;800&display=swap">
<style>
  :root{
    --canvas:#e6e6e4;
    --cover:#3cb99c;
    --cover-frame:#8fdccb;
    --title:#d9f3ec;
    --bracket:#17806a;
    --ink:#111;
    --white:#ffffff;
    --mint:#c6efe9;
    --mint-pale:#e9f9f6;
    --teal:#00ab8e;
    --teal-soft:#67d7c9;
    --blue:#0094d4;
    --text-dark:#3d4a48;
    --partner-navy:#23336b;
    --partner-red:#c7283a;
  }
  *{box-sizing:border-box;margin:0;padding:0}
  html,body{width:720px;height:1200px;overflow:hidden;background:var(--canvas)}
  body{position:relative;font-family:"Montserrat",Arial,sans-serif}

  .page{position:absolute;width:340px;height:440px;overflow:hidden}
  .cover{background:linear-gradient(170deg,#45c2a6 0%,var(--cover) 55%,#33b095 100%)}
  .cover-frame{position:absolute;left:14px;top:14px;right:14px;bottom:14px;border:1px solid var(--cover-frame);border-radius:16px;opacity:.7}

  .brand{position:absolute;display:flex;align-items:center;gap:10px}
  .brand-square{width:42px;height:42px;background:var(--ink)}
  .brand-name{font-weight:700;font-size:19px;color:var(--ink);letter-spacing:.3px}

  /* front cover */
  .front{left:370px;top:110px}
  .front .brand{left:38px;top:62px}
  .headline{position:absolute;left:30px;right:30px;top:170px;text-align:center;color:var(--title);font-weight:400}
  .headline .line1{font-weight:300;font-size:20px;letter-spacing:1px}
  .headline .line2{font-weight:700;font-size:27px;letter-spacing:.5px;line-height:1.05}
  .headline .line3{font-weight:800;font-size:36px;letter-spacing:.5px;line-height:1.05}
  .bracket{position:absolute;border-color:var(--bracket);border-style:solid;border-width:0}
  .bracket.tl{left:-6px;top:-8px;width:70px;height:24px;border-left-width:3px;border-top-width:3px}
  .bracket.tr{right:-6px;top:-8px;width:60px;height:22px;border-right-width:3px;border-top-width:3px}
  .bracket.br{right:-6px;top:72px;width:80px;height:28px;border-right-width:3px;border-bottom-width:3px}
  .bracket.bl{left:-6px;top:72px;width:40px;height:28px;border-left-width:3px;border-bottom-width:3px}

  .partners{position:absolute;display:flex;align-items:center;justify-content:space-between}
  .front .partners{left:26px;right:26px;bottom:26px}
  .partner{display:flex;align-items:center;gap:4px;font-weight:700;font-size:10px;white-space:nowrap}
  .partner .mark{width:8px;height:8px}
  .p-melta{color:var(--partner-navy)}.p-melta .mark{background:var(--partner-navy)}
  .p-quellon{color:var(--partner-red)}.p-quellon .mark{background:var(--partner-red)}
  .p-brevik{color:var(--blue)}.p-brevik .mark{background:var(--blue)}
  .p-talvix{color:var(--partner-navy)}.p-talvix .mark{background:var(--partner-red)}

  /* back cover */
  .back{left:20px;top:110px}
  .back-copy{position:absolute;left:26px;right:22px;top:34px;color:var(--white)}
  .back-copy .model{font-weight:700;font-size:8px;line-height:1.3}
  .back-copy .intro{font-size:6.3px;line-height:1.35;margin:8px 0 5px}
  .benefit{font-size:6.3px;line-height:1.35;margin-bottom:4px}
  .benefit strong{color:var(--bracket);font-weight:700}
  .offer{margin-top:10px;font-weight:700;font-size:10px;line-height:1.3}
  .site{font-weight:700;font-size:9.5px;margin-top:6px}
  .back .brand{left:26px;top:316px}
  .back .brand-square{width:34px;height:34px}
  .back .brand-name{font-size:16px}
  .back-band{position:absolute;left:0;right:0;bottom:0;height:62px;background:var(--white)}
  .back-band::before{content:"";position:absolute;left:0;right:0;top:0;height:4px;background:var(--mint)}
  .back-band::after{content:"";position:absolute;left:0;right:0;bottom:0;height:4px;background:var(--teal)}
  .back .partners{left:18px;right:18px;bottom:24px}

  /* inside spread */
  .inside-left{left:20px;top:600px;background:var(--white)}
  .inside-right{left:360px;top:600px;background:linear-gradient(180deg,#eef8f7,#f7fcfb)}
  .spread-fold{position:absolute;left:359px;top:600px;width:2px;height:440px;background:#d4e6e3}

  .site-render{position:absolute;left:0;top:0;width:340px;height:200px;background:linear-gradient(180deg,#6f8a78 0%,#88a673 45%,#b7c8b0 75%,#c9d2cf 100%)}
  .wave{position:absolute;left:0;top:150px;width:340px;height:70px}
  .melta-copy{position:absolute;left:18px;right:18px;top:212px;font-size:7.6px;line-height:1.45;color:var(--text-dark)}
  .melta-copy p{margin-bottom:5px}
  .melta-copy .lead{color:var(--teal);font-weight:700}
  .melta-copy ul{list-style:none;padding-left:4px;width:200px}
  .melta-copy li::before{content:"• "}
  .room-render{position:absolute;left:196px;top:334px;width:126px;height:62px;background:linear-gradient(180deg,#d9dddd,#a9b0b0)}
  .bottom-swoosh{position:absolute;left:0;bottom:0;width:340px;height:60px}

  .photo{position:absolute;border:3px solid var(--white);box-shadow:0 1px 3px rgba(0,0,0,.15)}
  .ph-tower{left:20px;top:92px;width:130px;height:150px;background:linear-gradient(180deg,#5f8fc4,#9bb7cf 55%,#7f9a78)}
  .ph-rack{left:92px;top:40px;width:120px;height:110px;background:linear-gradient(180deg,#c8cfcf,#6e7f58)}
  .ph-room{left:222px;top:60px;width:102px;height:66px;background:linear-gradient(180deg,#e3dfd2,#b39a62)}
  .ph-booth{left:140px;top:160px;width:124px;height:104px;background:linear-gradient(180deg,#9fb8d8,#aeb4b8 50%,#8c9296)}
  .ph-rack2{left:100px;top:230px;width:74px;height:86px;background:linear-gradient(180deg,#c2cac4,#6b7a56)}
  .ph-panels{left:236px;top:140px;width:96px;height:86px;background:linear-gradient(160deg,#f4f5f5,#d5d9d9)}
  .right-swoosh{position:absolute;left:0;bottom:0;width:340px;height:120px}
</style>
</head>
<body>

<!-- Back cover -->
<section class="page cover back" aria-label="Back cover">
  <div class="back-copy">
    <p class="model">Craft Growth Model<br>Advantages and Benefits<br>Updated: September 30, 2021</p>
    <p class="intro">Our cultivators enjoy several distinct advantages and benefits compared to conventional steel building or polycarbonate/glass greenhouse construction:</p>
    <p class="benefit"><strong>Build Faster.</strong> At least 12 weeks faster than conventional construction of the exterior and interior structure accelerating time to first harvest</p>
    <p class="benefit"><strong>Built Better.</strong> Deliver a fully engineered, code compliant, expandable and relocatable facility using our team of designers, manufacturers, and installers</p>
    <p class="benefit"><strong>Superior Grow Environment.</strong> Full blackout-controlled environment anchored by high-performance LED lights (PPF efficacy 2.85 µmol/J)</p>
    <p class="benefit"><strong>Airtight Facility.</strong> A sealed, airtight building solution critical for energy efficiency, maintaining CO2 levels and providing enhanced biosecurity</p>
    <p class="benefit"><strong>Reduced Energy Use.</strong> Tensioned membrane structure uses less energy than traditional structure, with electricity usage being consistent throughout facility</p>
    <p class="benefit"><strong>Increased Profits.</strong> Speed to market can generate almost $2.1 million in additional crop revenue, plus beat your licensee competitors to market</p>
    <p class="benefit"><strong>Financing.</strong> Qualified growers can receive interim and long-term financing from non-traditional sources for certain components of our integrated solution</p>
    <p class="benefit"><strong>Committed Team.</strong> Experienced vendor-partner team engaged in the process from beginning to end to assure your facility is completed and operational in a timely manner.</p>
    <p class="offer">Free Initial Consultation – $200 value<br>Please Have Advisor Contact Me</p>
    <p class="site">www.rivenstalkworks.com</p>
  </div>
  <div class="brand"><span class="brand-square"></span><span class="brand-name">Norvane Enterprises</span></div>
  <div class="back-band"></div>
  <div class="partners">
    <span class="partner p-melta"><span class="mark"></span>Melta-Brook</span>
    <span class="partner p-quellon"><span class="mark"></span>Quellon</span>
    <span class="partner p-brevik"><span class="mark"></span>Brevik</span>
    <span class="partner p-talvix"><span class="mark"></span>Talvix</span>
  </div>
</section>

<!-- Front cover -->
<section class="page cover front" aria-label="Front cover">
  <div class="cover-frame"></div>
  <div class="brand"><span class="brand-square"></span><span class="brand-name">Norvane Enterprises</span></div>
  <h1 class="headline">
    <span class="bracket tl"></span><span class="bracket tr"></span><span class="bracket br"></span><span class="bracket bl"></span>
    <span class="line1">WHEN SPEED TO</span><br>
    <span class="line2">MARKET COUNTS</span><br>
    <span class="line3">WE DELIVER</span>
  </h1>
  <div class="partners">
    <span class="partner p-melta"><span class="mark"></span>Melta-Brook</span>
    <span class="partner p-quellon"><span class="mark"></span>Quellon</span>
    <span class="partner p-brevik"><span class="mark"></span>Brevik</span>
    <span class="partner p-talvix"><span class="mark"></span>Talvix</span>
  </div>
</section>

<!-- Inside left: Melta-Brook -->
<section class="page inside-left" aria-label="Inside page, Melta-Brook">
  <div class="site-render" role="img" aria-label="Rendered aerial view of a cultivation campus with numbered buildings below a mountain ridge"></div>
  <svg class="wave" viewBox="0 0 340 70" preserveAspectRatio="none" aria-hidden="true">
    <path d="M0 62 C110 52 230 30 340 8 L340 70 L0 70 Z" fill="var(--white)"/>
    <path d="M0 58 C110 48 230 26 340 4 L340 10 C230 32 110 54 0 64 Z" fill="var(--teal)"/>
  </svg>
  <div class="melta-copy">
    <p><span class="lead">Melta-Brook</span> – When choosing between modular construction and traditionally constructed rooms, consider that all modular construction is objectively faster and more affordable.</p>
    <p>On average you can cut construction time by half when using a modular room and building design compared to conventionally construction.</p>
    <p>All components used to construct modular rooms and buildings have already been designed and fabricated at our plant, causing:</p>
    <ul>
      <li>Less disruption to your daily business operations</li>
      <li>Less construction waste and debris</li>
    </ul>
  </div>
  <div class="room-render" role="img" aria-label="Illustration of a modular room with windows"></div>
  <svg class="bottom-swoosh" viewBox="0 0 340 60" preserveAspectRatio="none" aria-hidden="true">
    <path d="M0 60 L0 44 C120 40 240 26 340 6 L340 60 Z" fill="var(--mint-pale)"/>
    <path d="M0 50 C120 46 240 32 340 12 L340 18 C240 38 120 52 0 56 Z" fill="var(--teal)"/>
    <path d="M0 58 C120 54 240 40 340 22 L340 25 C240 43 120 57 0 60 Z" fill="var(--teal-soft)"/>
  </svg>
</section>

<div class="spread-fold" aria-hidden="true"></div>

<!-- Inside right: Melta-Brook products -->
<section class="page inside-right" aria-label="Inside page, modular products">
  <div class="photo ph-tower" role="img" aria-label="Photo of a steel elevated guard tower"></div>
  <div class="photo ph-rack" role="img" aria-label="Photo of a drying room with hanging racks"></div>
  <div class="photo ph-room" role="img" aria-label="Photo of a lit modular grow room"></div>
  <div class="photo ph-booth" role="img" aria-label="Photo of a modular security booth"></div>
  <div class="photo ph-rack2" role="img" aria-label="Photo of a drying rack detail"></div>
  <div class="photo ph-panels" role="img" aria-label="Rendering of white modular wall panels"></div>
  <svg class="right-swoosh" viewBox="0 0 340 120" preserveAspectRatio="none" aria-hidden="true">
    <path d="M0 120 L0 96 C120 80 240 60 340 40 L340 120 Z" fill="var(--mint-pale)"/>
    <path d="M0 92 C120 76 240 56 340 36 L340 44 C240 64 120 84 0 100 Z" fill="var(--teal)"/>
    <path d="M0 104 C120 88 240 68 340 50 L340 54 C240 72 120 92 0 108 Z" fill="var(--teal-soft)"/>
  </svg>
</section>

</body>
</html>
```